BRISKWAY ELECTRICAL SIGN

We are wanting a sign to mount on the side of the road to attract peoples attention, it will be 1200mm high by 2400mm wide. We want it to stand out from the others, modern sharp looking, We are an electrical contractor who wants to be the market leader and supplier of choice to our current clients and futre clients.

Industry/Entity Type

Electrical

Colors

Designer to choose colors to be used in the design.

Requirements
Must have
• Name: Briskway Electrical
• Our logo as per uploaded files
• The words: Design - Installation - Maintenance
• Freecall: 0800 342 958
• Mobile : 021 736 4192 (delete mobile number if gets to cluttered)
• Web: www.briskway.net.nz
Should not have
• a light bulb, or plug

```html
<!DOCTYPE html>
<html lang="en">
<head>
<meta charset="utf-8">
<title>Briskway Electrical – Roadside Sign</title>
<link rel="stylesheet" href="https://fonts.googleapis.com/css2?family=Michroma&family=Oswald:wght@700&family=Montserrat:wght@600&display=swap">
<style>
  :root {
    --page: #e9e4e0;
    --navy-deep: #04244f;
    --navy: #0a3a72;
    --frame: #1d1d22;
    --ice: #e6f6fb;
    --aqua: #1ad3ee;
    --aqua-soft: #7ee6f4;
    --pill-start: #a8ecf3;
    --pill-end: #0ee3f6;
    --ink: #0a2a55;
  }
  * { box-sizing: border-box; margin: 0; padding: 0; }
  html, body { width: 1200px; height: 806px; overflow: hidden; }
  body { background: var(--page); position: relative; }

  .sign {
    position: absolute;
    left: 20px; top: 188px;
    width: 1160px; height: 430px;
    border: 4px solid var(--frame);
    background: var(--navy-deep);
    overflow: hidden;
  }
  .sign__backdrop {
    position: absolute; inset: 0;
    background:
      radial-gradient(ellipse 55% 70% at 82% 35%, rgba(40,120,190,.35), transparent 70%),
      radial-gradient(ellipse 40% 60% at 12% 80%, rgba(40,120,190,.25), transparent 70%),
      linear-gradient(180deg, var(--navy) 0%, var(--navy-deep) 100%);
  }
  .sign__content {
    position: relative;
    height: 100%;
    display: flex; flex-direction: column; align-items: center;
  }

  .brand {
    margin-top: 78px;
    display: flex; align-items: center; gap: 20px;
  }
  .brand__mark {
    width: 34px; height: 34px; border-radius: 50%;
    background: var(--aqua);
  }
  .brand__name {
    font-family: "Michroma", sans-serif;
    font-size: 50px;
    letter-spacing: 2px;
    color: var(--ice);
    white-space: nowrap;
  }

  .services {
    margin-top: 62px;
    display: flex; align-items: center;
    font-family: "Michroma", sans-serif;
    font-size: 20px;
    letter-spacing: 1px;
    color: var(--ice);
  }
  .services__item { padding: 0 30px; }
  .services__divider {
    width: 2px; height: 34px; background: var(--aqua);
  }

  .freecall {
    margin-top: 22px;
    width: 510px; height: 40px;
    border-radius: 20px;
    background: linear-gradient(90deg, var(--pill-start), var(--pill-end));
    display: flex; align-items: center; justify-content: center;
    font-family: "Oswald", sans-serif;
    font-weight: 700;
    font-size: 22px;
    letter-spacing: .5px;
    color: var(--ink);
  }

  .web {
    margin-top: 14px;
    font-family: "Montserrat", sans-serif;
    font-weight: 600;
    font-size: 20px;
    letter-spacing: 2px;
    color: var(--aqua);
  }
</style>
</head>
<body>
  <section class="sign" aria-label="Briskway Electrical roadside sign">
    <div class="sign__backdrop" role="img" aria-label="Dark blue background with faint network of connected lines and flowing wave lines"></div>
    <div class="sign__content">
      <div class="brand">
        <span class="brand__mark" aria-hidden="true"></span>
        <h1 class="brand__name">BRISKWAY ELECTRICAL</h1>
      </div>
      <ul class="services" style="list-style:none">
        <li class="services__item">DESIGN</li>
        <li class="services__divider" aria-hidden="true"></li>
        <li class="services__item">INSTALLATION</li>
        <li class="services__divider" aria-hidden="true"></li>
        <li class="services__item">MAINTENANCE</li>
      </ul>
      <p class="freecall">FREECALL: 0800 342 958</p>
      <p class="web">WWW.BRISKWAY.NET.NZ</p>
    </div>
  </section>
</body>
</html>
```